Hip Surgeon needs a web page re-design.

I have a web page to provide information about the diseases of the hip joint for the patients from my private practice since 2008. I need a re-design job for a fresh new look.
We have made a new logo and a new stationery design here in Marqueloft (please see the uploaded files) and I want to make my web page look-alike the new design concepts.
I like the color blue and tones of blue, matching my logo and stationery.
I don't like "busy" designs. It must be clean, elegant and ease to read. The final design should be "mobile friendly" if possible.
Please visit my website www.vilacorendasul.com.br to take a look and get some inspiration.

```html
<!DOCTYPE html>
<html lang="en">
<head>
<meta charset="utf-8">
<title>Dr. Rafael M. Tavares – Cirurgia do Quadril</title>
<link rel="stylesheet" href="https://fonts.googleapis.com/css2?family=Lato:ital,wght@0,400;0,700;1,400&display=swap">
<style>
:root{
  --blue:#1769b4;
  --blue-dark:#1a5aa0;
  --footer:#1d5eab;
  --footer-ink:#d3e3f6;
  --footer-head:#ffffff;
  --page:#f0f0f0;
  --white:#ffffff;
  --ink:#2b2b2b;
  --muted:#8a8a8a;
  --line:#dddddd;
  --panel:#ececec;
}
*{box-sizing:border-box;margin:0;padding:0}
html,body{width:835px;height:1200px;overflow:hidden}
body{position:relative;background:var(--page);font-family:'Lato',sans-serif;color:var(--ink)}
.abs{position:absolute}
.footer-band{left:0;top:976px;width:835px;height:224px;background:var(--footer)}
.card{left:104px;top:26px;width:626px;height:991px;background:var(--white);border-radius:0 0 6px 6px}
.logo-tab{left:141px;top:0;width:146px;height:75px;background:var(--white)}
.topbar{top:9px;left:490px;font-size:8px;display:flex;gap:14px;align-items:center}
.topbar .mail{color:var(--blue);border-left:1px solid #ccc;padding-left:10px}
.logo{left:146px;top:24px;display:flex;align-items:center;gap:6px;color:var(--blue)}
.logo .dot{width:28px;height:28px;border-radius:50%;background:var(--blue)}
.logo .name{font-size:14px;line-height:14px}
.logo .sub{font-size:10px;line-height:12px}
.nav{left:311px;top:40px;display:flex;gap:12px;font-size:8px;align-items:center}
.nav a{color:var(--ink);text-decoration:none}
.nav .active{background:var(--blue);color:#fff;padding:6px 8px;border-radius:2px}
.hero{left:104px;top:75px;width:444px;height:260px;background:linear-gradient(135deg,#7fa856 0%,#c9a585 40%,#6f8fc4 70%,#3f4c3a 100%)}
.hours{left:548px;top:75px;width:182px;height:260px;background:var(--blue);color:#fff;padding:14px 7px}
.hours h3{font-size:11px;font-weight:400;margin:0 0 12px 2px;display:flex;gap:6px;align-items:center}
.hours table{width:170px;border-collapse:collapse;font-size:6.5px;border:1px solid #5b9ad6}
.hours td{height:21px;padding-left:8px;border-bottom:1px solid #5b9ad6}
.hours tr:nth-child(odd){background:var(--blue-dark)}
.hours td:first-child{font-weight:700}
.hours .inq{font-size:11px;margin:20px 0 6px 2px;display:flex;gap:6px;align-items:center}
.hours .phones{font-size:11px;font-weight:700;margin-left:2px}
.feature{top:373px;width:170px;text-align:center}
.feature .icon{height:44px;display:flex;justify-content:center;align-items:flex-end}
.feature h4{font-size:8.5px;margin:9px 0 6px}
.feature p{font-size:7px;line-height:11.5px;color:var(--muted)}
h2{font-size:13px;font-weight:700}
.tip-photo{left:141px;top:545px;width:114px;height:155px;background:linear-gradient(180deg,#cfc4b6 0%,#e9e6e2 55%,#f4f4f4 100%)}
.tip-cap{left:141px;top:700px;width:114px;height:37px;background:var(--panel);text-align:center;font-size:7px;padding-top:8px}
.tip-cap em{color:var(--muted);display:block;margin-top:3px}
.tip{left:267px;top:544px;width:208px}
.tip h5{font-size:8.5px;color:#555;margin-bottom:9px}
.tip p{font-size:7px;line-height:13.5px;color:var(--muted);margin-bottom:8px}
.tip li{list-style:none;font-size:7px;color:#555;line-height:15.5px;display:flex;gap:6px;align-items:center}
.tip li::before{content:"";width:6px;height:6px;border-radius:50%;background:#555}
.btn{font-size:7px;padding:6px 5px;border:1px solid var(--blue);top:717px}
.btn.fill{background:var(--blue);color:#fff;left:267px}
.btn.line{left:433px;color:var(--ink);border-color:var(--blue-dark)}
.appt{left:516px;top:511px;width:178px;height:229px;background:var(--panel)}
.appt .head{background:var(--blue);color:#fff;font-size:8px;font-weight:700;height:25px;padding-left:12px;display:flex;align-items:center;gap:6px}
.field{position:absolute;left:10px;width:157px;height:21px;background:#fff;border:1px solid var(--line);font-size:6.5px;color:#666;padding:6px 6px}
.field .side{position:absolute;right:0;top:0;width:23px;height:19px;border-left:1px solid var(--line);display:flex;align-items:center;justify-content:center}
.submit{position:absolute;left:130px;top:197px;font-size:6.5px;border:1px solid var(--blue-dark);padding:5px 4px;background:#fff}
.faq-item{left:141px;width:271px;height:21px;background:var(--panel);font-size:7px;font-weight:700;display:flex;align-items:center}
.faq-item .tog{width:21px;height:21px;background:var(--blue);color:#fff;display:flex;align-items:center;justify-content:center;font-size:12px;margin-right:9px}
.faq-body{left:141px;top:831px;width:271px;height:57px;background:var(--panel)}
.faq-body .bar{position:absolute;left:0;top:0;width:21px;height:57px;background:#d8d8d8}
.faq-body p{position:absolute;left:30px;top:3px;width:236px;font-size:6.8px;line-height:11.8px;color:var(--muted)}
.surg{left:422px;width:270px;display:flex;gap:10px}
.surg .thumb{flex:none;width:54px;height:50px;border:1px solid var(--blue);background:linear-gradient(135deg,#d9c3a8,#b9573f 55%,#7a9bc0)}
.surg h6{font-size:8px;margin:4px 0 8px}
.surg p{font-size:7px;line-height:12px;color:var(--muted);width:205px}
.fcol{top:1040px;color:var(--footer-ink)}
.fcol h6{font-size:9px;font-weight:700;color:var(--footer-head);padding-bottom:6px;border-bottom:1px solid var(--footer-ink);display:inline-block;margin-bottom:10px}
.fcol ul{margin:0}
.fcol li{list-style:none;font-size:6.8px;line-height:15px;display:flex;gap:6px;align-items:center}
.fcol li.tick::before{content:"";width:6px;height:6px;background:var(--footer-ink)}
.fcol p{font-size:6.8px;line-height:11px;margin-bottom:6px}
.copy{left:141px;top:1184px;font-size:6.5px;color:#fff}
</style>
</head>
<body>
<div class="abs footer-band"></div>
<div class="abs card"></div>
<div class="abs logo-tab"></div>

<div class="abs topbar">
  <span style="display:flex;gap:5px;align-items:center">
    <svg width="9" height="9" viewBox="0 0 10 10"><rect width="10" height="10" rx="2" fill="#222"/><path d="M3 2.5l1 1.6-.7.7a4 4 0 0 0 2 2l.7-.7 1.6 1-.5 1C4.5 8 2 5.5 2 3z" fill="#fff"/></svg>
    41 3055 7180</span>
  <span class="mail">dr.rafael@vilacorendasul.com.br</span>
</div>

<div class="abs logo">
  <span class="dot"></span>
  <div><div class="name">Dr. Rafael M. Tavares</div><div class="sub">Cirurgia do Quadril</div></div>
</div>

<nav class="abs nav">
  <a class="active">HOME</a><a>SAIBA MAIS</a><a>CURRICULUM VITAE</a><a>LINKS</a><a>DOWNLOADS</a><a>ATUALIDADES</a><a>CONTACT</a>
</nav>

<div class="abs hero" role="img" aria-label="Photo of a smiling senior couple with bicycles outdoors"></div>

<aside class="abs hours">
  <h3><svg width="9" height="9" viewBox="0 0 10 10"><circle cx="5" cy="5" r="4" fill="none" stroke="#fff" stroke-width="1.3"/><path d="M5 2.6V5h2" stroke="#fff" stroke-width="1.2" fill="none"/></svg>Doctor's Time</h3>
  <table>
    <tr><td>Monday</td><td>09:00 am - 4:00 pm</td></tr>
    <tr><td>Tuesday</td><td>05:00 am - 10:00 pm</td></tr>
    <tr><td>Wednesday</td><td>Not Available</td></tr>
    <tr><td>Thursday</td><td>09:00 am - 4:00 pm</td></tr>
    <tr><td>Friday</td><td>09:00 am - 4:00 pm</td></tr>
    <tr><td>Saturday</td><td>09:00 am - 4:00 pm</td></tr>
    <tr><td>Sunday</td><td>Not Available</td></tr>
  </table>
  <div class="inq"><svg width="9" height="9" viewBox="0 0 10 10"><path d="M2 1l2 2.6-1 1.2a5 5 0 0 0 2.2 2.2l1.2-1L9 8l-1 1.6C4.5 9.6.4 5.5.4 2z" fill="#fff"/></svg>Inquiries</div>
  <div class="phones">41 3055 7180 (or)&nbsp; 41 3055 7181</div>
</aside>

<section class="abs feature" style="left:140px">
  <div class="icon"><svg width="30" height="30"><circle cx="15" cy="15" r="15" fill="#1769b4"/></svg></div>
  <h4>VEJA NOSSO CANAL</h4>
  <p>Lorem ipsum dolor sit amet, consectetur adipiscing elit. Etiam quis placerat urna. Nulla nulla diam, adipiscing non ornare non, commodo</p>
</section>
<section class="abs feature" style="left:346px">
  <div class="icon"><div role="img" aria-label="Hip joint illustration" style="width:36px;height:46px;background:var(--blue);border-radius:40% 50% 30% 45%"></div></div>
  <h4>PROSTHETIC HIP CARE</h4>
  <p>Este sucesso, porém, não depende apenas de nós cirurgiões. Os resultados alcançados serão tão melhores quanto maior for a sua motivação</p>
</section>
<section class="abs feature" style="left:521px">
  <div class="icon"><svg width="28" height="34" viewBox="0 0 28 34"><path d="M5 2v10a7 7 0 0 0 14 0V2M12 19v6a6 6 0 0 0 12 0v-5" fill="none" stroke="#1769b4" stroke-width="3"/><circle cx="24" cy="17" r="3" fill="none" stroke="#1769b4" stroke-width="2.5"/></svg></div>
  <h4>CONSULTATION</h4>
  <p>Lorem ipsum dolor sit amet, consectetur adipiscing elit. Etiam quis placerat urna. Nulla nulla diam, adipiscing non ornare non, commodo</p>
</section>

<h2 class="abs" style="left:141px;top:509px">Todays Tip from Dr. Rafael M. Tavares</h2>
<div class="abs tip-photo" role="img" aria-label="Portrait photo of the surgeon in a white coat"></div>
<div class="abs tip-cap"><strong>Rafael M.Tavares</strong><em>Cirurgia do Quadril</em></div>
<article class="abs tip">
  <h5>How to live a healthy lifestyle?</h5>
  <p>Etiam sit amet orci eget eros faucibus tincidunt. Duis leo. Sed fringilla mauris sit amet nibh. Donec sodales sagittis magna. Sed consequat, leo eget bibendum sodales, augue velit cursus nunc, quis gravida magna mi a libero. Etiam sit amet orci eget eros faucibus tincidunt. Duis leo.</p>
  <ul>
    <li>Dont just worry about the things you cannot help.</li>
    <li>Eat Healthy, work better, do gardening.</li>
    <li>Some relationships can kill you. Avoid them at the most.</li>
    <li>Focus on the good things that you like</li>
  </ul>
</article>
<span class="abs btn fill">PREV TIP</span>
<span class="abs btn line">NEXT TIP</span>

<form class="abs appt">
  <div class="head"><svg width="8" height="9" viewBox="0 0 8 9"><circle cx="4" cy="2.5" r="2" fill="#fff"/><path d="M0 9a4 4 0 0 1 8 0z" fill="#fff"/></svg>Book an Appointment</div>
  <div class="field" style="top:40px">Select Department<span class="side"><svg width="6" height="4"><path d="M0 0h6L3 4z" fill="#1769b4"/></svg></span></div>
  <div class="field" style="top:72px">Your Name (required)</div>
  <div class="field" style="top:103px">Your Phone (required)</div>
  <div class="field" style="top:135px">Email (required)</div>
  <div class="field" style="top:166px">Date of Appointment<span class="side"><svg width="8" height="8"><rect x=".5" y="1.5" width="7" height="6" fill="none" stroke="#1769b4"/><rect x="0" y="1" width="8" height="2" fill="#1769b4"/></svg></span></div>
  <span class="submit">SUBMIT</span>
</form>

<h2 class="abs" style="left:141px;top:770px">FAQ's</h2>
<div class="abs faq-item" style="top:810px"><span class="tog">–</span>How to diagnose osteoporosis?</div>
<div class="abs faq-body"><span class="bar"></span><p>Symptoms appear in derivations of fractures of the wrist, pelvis, hip, ribs or micro fractures of the spine that can lead to chronic pain and even to what we call rigid kyphosis or "dowager's hump" caused by the loss of height of the vertebrae.</p></div>
<div class="abs faq-item" style="top:894px"><span class="tog">+</span>What are the symptoms of the impact?</div>
<div class="abs faq-item" style="top:920px"><span class="tog">+</span>How to diagnose femoral acetabular labral injury or impact?</div>
<div class="abs faq-item" style="top:946px"><span class="tog">+</span>What causes pubalgia?</div>

<h2 class="abs" style="left:423px;top:770px">Hip Surgeries</h2>
<div class="abs surg" style="top:809px"><div class="thumb" role="img" aria-label="Illustration of a pelvis fracture"></div><div><h6>Fractures of the Pelvis and Acetabulum</h6><p>Fractures of the acetabulum involving the hip joint region. As well as pelvic fractures may occur in the elderly by minor trauma.</p></div></div>
<div class="abs surg" style="top:866px"><div class="thumb" role="img" aria-label="Illustration of hip arthroscopy"></div><div><h6>Hip Arthroscopy</h6><p>The surgery can be performed with spinal anesthesia and sedation or general anesthesia.</p></div></div>
<div class="abs surg" style="top:923px"><div class="thumb" role="img" aria-label="Illustration of a hip prosthesis"></div><div><h6>Hip Prosthesis</h6><p>Prosthetic hip (or hip arthroplasty) surgery is performed in order to replace the hip joint.</p></div></div>

<div class="abs fcol" style="left:141px"><h6>HEALTH SOLUTIONS</h6><ul>
  <li class="tick">Hip Arthroscopy</li><li class="tick">Osteoarthritis</li><li class="tick">Bursitis and Tendinitis</li><li class="tick">Osteonecrosis</li><li class="tick">Osteoporosis</li><li class="tick">Hip Prosthesis (arthroplasty)</li><li class="tick">Rebound hip (snapping hip)</li></ul></div>
<div class="abs fcol" style="left:266px;width:150px"><h6>RECENT NEWS</h6>
  <p>Hip Preservation in the Adolescent and Young Adult - NAJS - Lakeview 2013</p>
  <p>4th Annual Scientific Meeting - Global Forum for Hip Arthroscopy - Harborton 2012</p>
  <p>The "impact of impact" in hip arthroplasty</p>
  <p>Current Concepts in Joint Replacement - Silver Bay 2012</p></div>
<div class="abs fcol" style="left:425px;width:110px"><h6>LINKS</h6>
  <p>Sociedade Nacional de Ortopedia Clínica</p>
  <p>Associação Regional do Quadril</p>
  <p>Northbridge Academy of Joint Surgeons</p></div>
<div class="abs fcol" style="left:550px;width:140px"><h6>CONTACT INFO</h6>
  <p>Rua das Acácias, 512 - Jardim Azul - Vila Serena / PR</p>
  <p style="margin-top:8px"><strong>Phone :</strong> 41 3055 7180<br><span style="padding-left:35px">: 41 3055 7181</span></p></div>
<div class="abs copy">Copyright information here</div>
</body>
</html>
```